Business Card Design

Great brand name mattresses at bulk prices, quality affordable for everyone.

something relating to a mattress is important for the card please.

Industry/Entity Type

Business

Contact Information for Business Card

Corvane Mattress

Requirements
Must have
• something related to a mattress, its the only thing we sell… the logo is not mandatory but would like, i understand the logo does not have a mattress

```html
<!DOCTYPE html>
<html lang="en">
<head>
<meta charset="utf-8">
<title>Corvane Mattress – Business Cards</title>
<link rel="stylesheet" href="https://fonts.googleapis.com/css2?family=Arvo:wght@700&family=Josefin+Slab:wght@600&family=Questrial&display=swap">
<style>
  :root {
    --backdrop: #ebe8e3;
    --card-white: #ffffff;
    --ink: #1d1a18;
    --brand-blue: #1584d8;
    --sky-blue: #5bbff7;
    --stripe-blue: #1a7fd6;
    --icon-blue: #4ab3ee;
    --tag-black: #1c1c1c;
  }
  * { box-sizing: border-box; margin: 0; padding: 0; }
  html, body {
    width: 1200px; height: 900px; overflow: hidden;
    background: var(--backdrop);
  }
  .canvas { position: relative; width: 1200px; height: 900px; }

  .card {
    position: absolute; width: 356px; height: 608px;
    box-shadow: 0 2px 10px rgba(0,0,0,0.18);
  }
  .card--back-left { left: 52px; top: 212px; background: var(--card-white); }
  .card--back-right { left: 791px; top: 212px; background: var(--card-white); }
  .card--front { left: 425px; top: 78px; background: var(--sky-blue); overflow: hidden; }

  .wordmark {
    position: absolute; left: 0; right: 0; top: 40px;
    text-align: center;
    font-family: "Arvo", Georgia, serif; font-weight: 700;
    font-size: 44px; line-height: 50px; letter-spacing: 1px;
    color: var(--ink); text-transform: uppercase;
  }
  .card--front .wordmark { color: var(--card-white); }

  .people {
    position: absolute; left: 0; right: 0; top: 216px;
    text-align: center;
    font-family: "Josefin Slab", Georgia, serif; font-weight: 600;
    font-size: 18px; line-height: 29px; color: var(--brand-blue);
  }
  .card--back-right .people { font-variant: small-caps; letter-spacing: 0.5px; }

  .contact {
    position: absolute; left: 0; right: 0; top: 360px;
    text-align: center;
    font-family: "Questrial", Arial, sans-serif;
    font-size: 14px; line-height: 20px; color: var(--ink);
  }
  .contact__group { margin-bottom: 10px; }
  .contact__icon { display: block; margin: 0 auto 8px; width: 26px; height: 26px; }

  .front-art { position: absolute; left: 0; top: 0; }
  .offer {
    position: absolute; font-family: "Josefin Slab", Georgia, serif; font-weight: 600;
    background: var(--tag-black); padding: 4px 18px;
  }
  .offer--brands {
    left: 62px; top: 520px; font-size: 25px; color: var(--stripe-blue);
    transform: rotate(-12deg);
  }
  .offer--discount {
    left: 134px; top: 552px; font-size: 22px; color: var(--card-white);
    font-family: "Questrial", Arial, sans-serif; padding: 6px 18px 6px 38px;
    transform: rotate(-2deg);
  }
</style>
</head>
<body>
<main class="canvas">

  <section class="card card--back-left">
    <div class="wordmark">Corvane<br>Mattress</div>
    <div class="people">Mateo Ferreira<br>Andres Ferreira</div>
    <div class="contact">
      <div class="contact__group">
        <svg class="contact__icon" viewBox="0 0 26 26"><path d="M13 3 L2 13 H5 V23 H11 V17 H15 V23 H21 V13 H24 Z" fill="var(--icon-blue)"/></svg>
        4210 SW, 152 Street, Unit 18, Corvane, FL 30412<br>73 NW, 128 Street, Corvane, FL 30418
      </div>
      <div class="contact__group">
        <svg class="contact__icon" viewBox="0 0 26 26"><circle cx="13" cy="13" r="11.5" fill="none" stroke="var(--icon-blue)" stroke-width="1.5"/><path d="M10 6 L12 10 L10.5 11.5 Q12 15 14.5 16 L16 14.5 L20 16.5 L18.5 19.5 Q11 19 7.5 9 Z" fill="var(--icon-blue)"/></svg>
        (555) 210 4836<br>(555) 382 0915
      </div>
      <div class="contact__group">
        <svg class="contact__icon" viewBox="0 0 26 26" fill="none" stroke="var(--icon-blue)" stroke-width="1.5"><circle cx="13" cy="13" r="11"/><ellipse cx="13" cy="13" rx="5" ry="11"/><path d="M2 13 H24 M4 7.5 H22 M4 18.5 H22"/></svg>
        info@corvanemattress.com<br>www.corvanemattress.com
      </div>
    </div>
  </section>

  <section class="card card--front">
    <svg class="front-art" width="356" height="608" viewBox="0 0 356 608">
      <polygon points="0,192 356,152 356,164 0,204" fill="var(--stripe-blue)"/>
      <polygon points="0,204 356,164 356,470 0,510" fill="#d9dde2" role="img" aria-label="Photo of a tall stack of white and grey quilted mattresses"/>
      <polygon points="0,510 356,470 356,478 0,518" fill="var(--stripe-blue)"/>
    </svg>
    <div class="wordmark">Corvane<br>Mattress</div>
    <div class="offer offer--brands">Best Brands</div>
    <div class="offer offer--discount">75% OFF</div>
  </section>

  <section class="card card--back-right">
    <div class="wordmark">Corvane<br>Mattress</div>
    <div class="people">Mateo Ferreira<br>Andres Ferreira</div>
    <div class="contact">
      <div class="contact__group">
        <svg class="contact__icon" viewBox="0 0 26 26"><path d="M13 3 L2 13 H5 V23 H11 V17 H15 V23 H21 V13 H24 Z" fill="var(--icon-blue)"/></svg>
        4210 SW, 152 Street, Unit 18, Corvane, FL 30412<br>73 NW, 128 Street, Corvane, FL 30418
      </div>
      <div class="contact__group">
        <svg class="contact__icon" viewBox="0 0 26 26"><circle cx="13" cy="13" r="11.5" fill="none" stroke="var(--icon-blue)" stroke-width="1.5"/><path d="M10 6 L12 10 L10.5 11.5 Q12 15 14.5 16 L16 14.5 L20 16.5 L18.5 19.5 Q11 19 7.5 9 Z" fill="var(--icon-blue)"/></svg>
        (555) 210 4836<br>(555) 382 0915
      </div>
      <div class="contact__group">
        <svg class="contact__icon" viewBox="0 0 26 26" fill="none" stroke="var(--icon-blue)" stroke-width="1.5"><circle cx="13" cy="13" r="11"/><ellipse cx="13" cy="13" rx="5" ry="11"/><path d="M2 13 H24 M4 7.5 H22 M4 18.5 H22"/></svg>
        info@corvanemattress.com<br>www.corvanemattress.com
      </div>
    </div>
  </section>

</main>
</body>
</html>
```